Trade Show Flier for CleanTech Battery Company
Halden Vore Partners
Company Overview, Corporate Partners, Product Specifications
Halden Vore Partners is a cleantech startup developing large commercial size redox flow batteries. These batteries are used for providing backup power to buildings and for helping to integrate solar and wind energy into the electricity grid.
Energy
Corporate - will distribute fliers at trade show to potential partners, investors, researchers, etc.
Want a clean & modern look. See www.haldenvorepartners.example for corporate colors and design theme. Template will be used for a variety of materials such as specifications sheet, corporate overview, etc.
HVP Corporate Logo
HVP Corporate Name and Logo

```html
<!DOCTYPE html>
<html lang="en">
<head>
<meta charset="utf-8">
<title>Halden Vore Partners – Trade Show Flier</title>
<link rel="stylesheet" href="https://fonts.googleapis.com/css2?family=Open+Sans:ital,wght@0,400;0,600;0,700;0,800;1,400;1,600&display=swap">
<style>
:root{
  --navy:#173a74;
  --blue:#2457a6;
  --sky:#3f7cc8;
  --pale:#e4edf7;
  --rule:#b9cbe2;
  --ink:#3a3f47;
  --paper:#ffffff;
  --stage:#e9ebee;
  --green:#59b14a;
}
*{box-sizing:border-box;margin:0;padding:0}
html,body{width:1200px;height:511px;overflow:hidden;background:var(--stage);font-family:"Open Sans",Arial,sans-serif;color:var(--ink)}
.spread{position:absolute;top:12px;width:576px;height:488px;background:var(--paper);box-shadow:0 2px 6px rgba(0,0,0,.25);overflow:hidden}
.spread--front{left:20px}
.spread--inside{left:606px}
.fold{position:absolute;top:0;bottom:0;left:288px;width:1px;background:rgba(0,0,0,.08);z-index:2}
.abs{position:absolute}
.photo{position:absolute}
/* front */
.brand{left:14px;top:14px;display:flex;align-items:center;gap:6px}
.brand__dot{width:26px;height:26px;border-radius:50%;background:var(--blue)}
.brand__name{font-weight:800;font-size:22px;color:var(--navy);letter-spacing:.5px}
.brand__tag{left:14px;top:46px;font-size:6px;color:var(--blue);width:110px}
.photo--hands{left:210px;top:0;width:366px;height:200px;background:linear-gradient(135deg,#dce9f6 0%,#a9c6e6 50%,#6f99cc 100%)}
.headline{left:14px;top:152px;width:188px;font-size:14px;line-height:1.22;font-weight:700;color:var(--navy)}
.section-title{display:flex;align-items:center;gap:6px;font-weight:700;color:var(--navy);font-size:11.5px}
.section-title__icon{width:16px;height:16px;border-radius:50%;background:var(--blue);flex:none}
.body{font-size:6.2px;line-height:1.45;color:var(--ink)}
.panel{background:var(--navy);color:#fff;padding:12px 14px}
.panel ul{list-style:none}
.panel li{font-size:6.8px;line-height:1.35;margin-bottom:5px;display:flex;gap:6px;align-items:center}
.panel li::before{content:"";width:4px;height:4px;background:#8fb7e8;flex:none}
.spec-row{display:flex;gap:6px;align-items:center;height:20px;border-bottom:1px solid var(--rule)}
.spec-row__label{flex:1;font-size:6.5px;color:var(--ink)}
.spec-row__cell{width:26px;height:12px;background:var(--navy)}
.spec-row__cell--light{background:var(--sky)}
.photo--canyon{left:302px;top:414px;width:260px;height:62px;background:linear-gradient(135deg,#a9c2e2 0%,#c58a63 55%,#9c4a27 100%)}
/* inside */
.photo--desert{left:0;top:0;width:576px;height:205px;background:linear-gradient(135deg,#6f97cf 0%,#b98567 55%,#a5532c 100%)}
.intro-band{left:288px;top:0;width:288px;height:86px;background:var(--navy);color:#fff;padding:10px 14px;font-size:7.4px;font-weight:700;line-height:1.38}
.model-table{border-collapse:collapse;width:250px;font-size:6px}
.model-table th{background:var(--navy);color:#fff;font-weight:600;padding:4px;text-align:left}
.model-table td{padding:3.5px 4px;border-bottom:1px solid var(--rule)}
.model-table tr:nth-child(even) td{background:var(--pale)}
.chip{background:var(--blue);color:#fff;font-size:6.5px;padding:5px 8px;margin-bottom:5px;display:flex;justify-content:space-between;align-items:center}
.chip__swatch{width:12px;height:8px;background:var(--green)}
.quote{font-style:italic;font-weight:600;color:var(--blue);font-size:7.2px;line-height:1.4}
.legend{display:flex;gap:10px;font-size:6px}
.legend span{display:flex;align-items:center;gap:3px}
.legend i{width:8px;height:6px;display:inline-block}
</style>
</head>
<body>

<section class="spread spread--front">
  <div class="photo photo--hands" role="img" aria-label="Photo of cupped hands holding a glass globe with a tree inside"></div>
  <div class="abs brand"><span class="brand__dot"></span><span class="brand__name">HVP</span></div>
  <p class="abs brand__tag">Halden Vore Partners</p>
  <h1 class="abs headline">Novel flow battery technology for commercial, industrial and utility applications</h1>

  <div class="abs" style="left:14px;top:252px;width:262px">
    <h2 class="section-title"><span class="section-title__icon"></span>Halden Vore Partners Inc.</h2>
    <p class="body" style="margin-top:8px">Halden Vore Partners (HVP) designs redox flow batteries for commercial, industrial and utility sites. Our systems store solar and wind energy and deliver reliable backup power for buildings and the grid.</p>
  </div>

  <div class="abs panel" style="left:0;top:350px;width:288px;height:138px">
    <ul>
      <li>Long duration storage for commercial sites</li>
      <li>Safe, non-flammable aqueous chemistry</li>
      <li>Scalable from kilowatts to megawatts</li>
      <li>Twenty year design life</li>
      <li>Low cost per stored kilowatt hour</li>
      <li>Grid integration for solar and wind</li>
    </ul>
  </div>

  <div class="fold"></div>

  <div class="abs" style="left:302px;top:214px;width:260px">
    <h2 class="section-title"><span class="section-title__icon"></span>Lorem Ipsum Dolor Set Emet</h2>
    <div style="margin-top:6px">
      <div class="spec-row"><span class="spec-row__label">Rated power output</span><span class="spec-row__cell"></span><span class="spec-row__cell spec-row__cell--light"></span></div>
      <div class="spec-row"><span class="spec-row__label">Storage capacity</span><span class="spec-row__cell"></span><span class="spec-row__cell spec-row__cell--light"></span></div>
      <div class="spec-row"><span class="spec-row__label">Round trip efficiency</span><span class="spec-row__cell"></span><span class="spec-row__cell spec-row__cell--light"></span></div>
      <div class="spec-row"><span class="spec-row__label">Cycle life</span><span class="spec-row__cell"></span><span class="spec-row__cell spec-row__cell--light"></span></div>
    </div>
    <h2 class="section-title" style="margin-top:14px"><span class="section-title__icon"></span>Lorem Ipsum Dolor</h2>
    <p class="body" style="margin-top:6px">Modular tanks and stacks install quickly and grow with demand over time.</p>
  </div>
  <div class="photo photo--canyon" role="img" aria-label="Photo of a red rock canyon landscape"></div>
</section>

<section class="spread spread--inside">
  <div class="photo photo--desert" role="img" aria-label="Photo of red desert rock formations under a blue sky"></div>
  <div class="abs intro-band">Lorem ipsum dolor sit amet, consectetur adipiscing elit, sed do eiusmod tempor incididunt ut labore et dolore magna aliqua. Ut enim ad minim veniam, quis nostrud exercitation ullamco laboris nisi ut aliquip ex ea commodo consequat.</div>

  <div class="abs" style="left:16px;top:216px;width:256px">
    <p class="body">Halden Vore Partners (HVP) builds flow batteries that shift renewable energy to peak hours, cut demand charges and keep critical loads running during outages. Each system is sized to the site.</p>
    <table class="model-table" style="margin-top:12px">
      <tr><th>Model</th><th>kW</th><th>kWh</th><th>Hours</th></tr>
      <tr><td>HVP-50</td><td>50</td><td>200</td><td>4</td></tr>
      <tr><td>HVP-100</td><td>100</td><td>400</td><td>4</td></tr>
      <tr><td>HVP-250</td><td>250</td><td>1000</td><td>4</td></tr>
      <tr><td>HVP-500</td><td>500</td><td>3000</td><td>6</td></tr>
      <tr><td>HVP-1000</td><td>1000</td><td>8000</td><td>8</td></tr>
    </table>
  </div>

  <div class="fold"></div>

  <div class="abs" style="left:302px;top:216px;width:130px">
    <h2 class="section-title"><span class="section-title__icon"></span>Cost Comparison Chart</h2>
    <svg width="130" height="140" viewBox="0 0 130 140" style="margin-top:8px">
      <g stroke="#d5dde8" stroke-width="0.6">
        <line x1="14" y1="10" x2="128" y2="10"/><line x1="14" y1="40" x2="128" y2="40"/>
        <line x1="14" y1="70" x2="128" y2="70"/><line x1="14" y1="100" x2="128" y2="100"/>
      </g>
      <line x1="14" y1="130" x2="128" y2="130" stroke="#7f8a99" stroke-width="0.8"/>
      <g fill="#59b14a">
        <rect x="18" y="90" width="7" height="40"/><rect x="40" y="80" width="7" height="50"/>
        <rect x="62" y="66" width="7" height="64"/><rect x="84" y="50" width="7" height="80"/>
        <rect x="106" y="36" width="7" height="94"/>
      </g>
      <g fill="#2457a6">
        <rect x="26" y="76" width="7" height="54"/><rect x="48" y="62" width="7" height="68"/>
        <rect x="70" y="44" width="7" height="86"/><rect x="92" y="26" width="7" height="104"/>
        <rect x="114" y="12" width="7" height="118"/>
      </g>
    </svg>
    <div class="legend" style="margin-top:4px"><span><i style="background:var(--green)"></i>Flow battery</span><span><i style="background:var(--blue)"></i>Lithium ion</span></div>
  </div>

  <div class="abs" style="left:442px;top:216px;width:122px">
    <div class="chip">Lorem ipsum dolor sit<span class="chip__swatch"></span></div>
    <div class="chip">Lorem ipsum dolor sit<span class="chip__swatch" style="background:#9fd18f"></span></div>
    <div class="chip">Lorem ipsum dolor sit<span class="chip__swatch" style="background:#8fb7e8"></span></div>
    <p class="body" style="margin-top:6px">Flow batteries keep their capacity for thousands of cycles, so the cost per stored kilowatt hour falls steadily over the life of each installation.</p>
  </div>

  <p class="abs quote" style="left:302px;top:414px;width:262px">Lorem ipsum dolor sit amet, consectetur adipiscing elit, sed do eiusmod tempor incididunt ut labore et dolore magna aliqua. Ut enim ad minim veniam, quis nostrud exercitation ullamco laboris nisi ut aliquip ex ea commodo consequat.</p>
</section>

</body>
</html>
```